Insurance Firm needs Stationary and Corporate Identity

We have a logo (provided) - we need a business card, letterhead, booklet cover, Benefit & Travel card design, and brand guide.
LRC (Larkmoor Relief Cooperative) is a National (Canadian) family-run benefits firm. We've been providing alternative benefit models to small and medium sized businesses for almost 25 years! Our goal is to create long-lasting customer relationships by partnering with our clients to become their dedicated benefits division instead of just selling a product to them.

Benefit & Travel Cards: We provide the benefit card to employees to allow them to pay for drugs at their pharmacy and dental services electronically.
The travel card is for medical emergencies while travelling outside of Canada.

Brand Guide: Once the stationary is complete, the brand guide will allow us to streamline the use of our logo's and fonts for internal and external use. We will expect that this will be a paid project for our design winner after the contest closes and we will negotiate the pricetag for this at that time.

Target Market(s)

Business Owners, Entrepreneurs, HR Professionals

Industry/Entity Type

Insurance Agency

Font styles to use
Sans Serif

Requirements
Must have
• business card, letterhead, health card, travel card, booklet cover (some current samples provided)

```html
<!DOCTYPE html>
<html lang="en">
<head>
<meta charset="utf-8">
<title>Larkmoor Relief Cooperative — Stationery Set</title>
<link href="https://fonts.googleapis.com/css2?family=Lato:wght@400;700&family=PT+Serif:wght@400;700&display=swap" rel="stylesheet">
<style>
  :root {
    --navy: #2e3a4e;
    --navy-deep: #232e3e;
    --navy-panel: #34425a;
    --red: #d9302a;
    --red-bright: #e8262b;
    --red-deep: #b8181a;
    --grey: #8d9096;
    --white: #ffffff;
    --stage-light: #f2f2f2;
    --stage-dark: #9a9a9a;
  }
  * { margin: 0; padding: 0; box-sizing: border-box; }
  html, body { width: 1200px; height: 1000px; overflow: hidden; }
  body {
    background: radial-gradient(ellipse at 35% 30%, var(--stage-light) 0%, #d6d6d6 55%, var(--stage-dark) 100%);
    position: relative;
    font-family: "PT Serif", serif;
  }
  .piece {
    position: absolute;
    box-shadow: 0 14px 26px rgba(0,0,0,0.35);
  }
  .piece svg { display: block; width: 100%; height: 100%; }
  .sans { font-family: "Lato", sans-serif; }
  .serif { font-family: "PT Serif", serif; }
  .card-front { left: 74px; top: 53px; width: 354px; height: 203px; }
  .card-back { left: 76px; top: 299px; width: 352px; height: 201px; }
  .travel-card { left: 441px; top: 199px; width: 351px; height: 200px; }
  .health-card { left: 804px; top: 54px; width: 353px; height: 202px; }
  .card-split { left: 804px; top: 299px; width: 353px; height: 201px; }
  .booklet-cover { left: 212px; top: 555px; width: 251px; height: 355px; }
  .letterhead { left: 658px; top: 559px; width: 247px; height: 351px; }
</style>
</head>
<body>

<!-- Business card front -->
<div class="piece card-front">
  <svg viewBox="0 0 354 203">
    <rect width="354" height="203" fill="var(--navy)"/>
    <rect x="0" width="20" height="203" fill="var(--navy-deep)"/>
    <rect x="38" width="26" height="203" fill="var(--navy-deep)"/>
    <rect x="290" width="26" height="203" fill="var(--navy-deep)"/>
    <rect x="334" width="20" height="203" fill="var(--navy-deep)"/>
    <polygon points="0,22 64,28 64,140 0,150" fill="var(--red-deep)"/>
    <polygon points="354,22 290,28 290,140 354,150" fill="var(--red-deep)"/>
    <polygon points="38,26 64,28 64,140 38,144" fill="#cc2320"/>
    <polygon points="316,26 290,28 290,140 316,144" fill="#cc2320"/>
    <rect x="64" y="28" width="226" height="112" fill="var(--red)"/>
    <ellipse cx="181" cy="114" rx="30" ry="6" fill="var(--red-deep)"/>
    <circle cx="181" cy="87" r="31" fill="var(--navy)"/>
    <text x="181" y="95" text-anchor="middle" class="sans" font-size="22" font-weight="700" fill="var(--white)">LRC</text>
    <text x="181" y="172" text-anchor="middle" class="sans" font-size="11.5" font-weight="700" fill="var(--red)">LARKMOOR RELIEF</text>
    <line x1="113" y1="183" x2="131" y2="183" stroke="var(--grey)" stroke-width="1"/>
    <line x1="231" y1="183" x2="249" y2="183" stroke="var(--grey)" stroke-width="1"/>
    <text x="181" y="187" text-anchor="middle" class="sans" font-size="10" fill="var(--grey)">COOPERATIVE</text>
  </svg>
</div>

<!-- Business card back -->
<div class="piece card-back">
  <svg viewBox="0 0 352 201">
    <rect width="352" height="201" fill="var(--navy)"/>
    <rect x="0" width="20" height="201" fill="var(--navy-deep)"/>
    <rect x="332" width="20" height="201" fill="var(--navy-deep)"/>
    <rect x="0" y="0" width="352" height="22" fill="var(--red)"/>
    <polygon points="0,22 64,22 64,40 0,30" fill="var(--red-deep)" opacity="0.6"/>
    <polygon points="352,22 288,22 288,40 352,30" fill="var(--red-deep)" opacity="0.6"/>
    <rect x="64" y="22" width="224" height="164" fill="var(--navy-panel)"/>
    <rect x="0" y="186" width="352" height="15" fill="var(--navy-deep)"/>
    <text transform="translate(86,128) rotate(-90)" class="sans" font-size="10" font-weight="700" fill="var(--red)">LARKMOOR RELIEF</text>
    <text transform="translate(98,122) rotate(-90)" class="sans" font-size="8" fill="var(--grey)">COOPERATIVE</text>
    <line x1="107" y1="40" x2="107" y2="170" stroke="var(--grey)" stroke-width="1.2"/>
    <circle cx="87" cy="162" r="13" fill="var(--navy-deep)"/>
    <text x="87" y="165" text-anchor="middle" class="sans" font-size="8" font-weight="700" fill="var(--white)">LRC</text>
    <g class="serif" fill="var(--white)" text-anchor="end">
      <text x="248" y="64" font-size="12" font-weight="700">Maren Tolliver</text>
      <text x="248" y="74" font-size="9">Creative Design</text>
      <text x="248" y="98" font-size="10" font-weight="700">555 010 0000</text>
      <text x="248" y="126" font-size="10" font-weight="700">Your location</text>
      <text x="248" y="152" font-size="10" font-weight="700">tolliver@lrc.com</text>
    </g>
    <g fill="var(--red)">
      <rect x="254" y="54" width="22" height="22" rx="3"/>
      <rect x="254" y="83" width="22" height="22" rx="3"/>
      <rect x="254" y="111" width="22" height="22" rx="3"/>
      <rect x="254" y="138" width="22" height="22" rx="3"/>
    </g>
    <g fill="var(--white)">
      <circle cx="265" cy="62" r="3"/>
      <path d="M259 71 a6 5 0 0 1 12 0 z"/>
      <path d="M259 89 l3 -1 2 3 -1.5 1.5 a7 7 0 0 0 4 4 l1.5 -1.5 3 2 -1 3 c-6 0 -11 -5 -11 -11z"/>
      <path d="M265 115 a4 4 0 0 1 4 4 c0 3 -4 7 -4 7 s-4 -4 -4 -7 a4 4 0 0 1 4 -4z"/>
      <rect x="259" y="143" width="12" height="12" rx="1"/>
    </g>
    <circle cx="265" cy="119" r="1.5" fill="var(--red)"/>
    <path d="M260 144 l5 5 5 -5" stroke="var(--red)" fill="none" stroke-width="1.2"/>
  </svg>
</div>

<!-- Travel card -->
<div class="piece travel-card">
  <svg viewBox="0 0 351 200">
    <rect width="351" height="200" fill="var(--navy)"/>
    <polygon points="0,30 52,20 52,82 0,90" fill="var(--red-deep)"/>
    <polygon points="351,30 299,20 299,82 351,90" fill="var(--red-deep)"/>
    <rect x="52" y="20" width="247" height="62" fill="var(--red)"/>
    <rect x="0" y="82" width="351" height="118" fill="var(--navy-deep)"/>
    <rect x="30" y="100" width="310" height="80" fill="var(--navy)" opacity="0.85" role="img" aria-label="Faint world map backdrop"/>
    <circle cx="176" cy="51" r="19" fill="var(--navy)"/>
    <text x="176" y="55" text-anchor="middle" class="sans" font-size="10" font-weight="700" fill="var(--white)">LRC</text>
    <text x="176" y="97" text-anchor="middle" class="sans" font-size="9" font-weight="700" fill="var(--red)">LARKMOOR RELIEF</text>
    <line x1="140" y1="106" x2="150" y2="106" stroke="var(--grey)"/>
    <line x1="202" y1="106" x2="212" y2="106" stroke="var(--grey)"/>
    <text x="176" y="109" text-anchor="middle" class="sans" font-size="7.5" fill="var(--grey)">COOPERATIVE</text>
    <g fill="var(--red)">
      <rect x="41" y="121" width="18" height="18" rx="3"/>
      <rect x="41" y="143" width="18" height="18" rx="3"/>
      <rect x="41" y="165" width="18" height="18" rx="3"/>
    </g>
    <g fill="var(--white)">
      <circle cx="50" cy="127" r="2.5"/>
      <path d="M45 135 a5 4 0 0 1 10 0z"/>
      <path d="M45 148 l2.5 -1 1.5 2.5 -1 1 a6 6 0 0 0 3 3 l1 -1 2.5 1.5 -1 2.5 c-5 0 -8.5 -3.5 -8.5 -8.5z"/>
      <path d="M50 169 a3.5 3.5 0 0 1 3.5 3.5 c0 2.5 -3.5 6 -3.5 6 s-3.5 -3.5 -3.5 -6 a3.5 3.5 0 0 1 3.5 -3.5z"/>
    </g>
    <g class="serif" fill="var(--white)">
      <text x="81" y="130" font-size="10" font-weight="700">Maren Tolliver</text>
      <text x="81" y="141" font-size="7.5">Creative Design</text>
      <text x="81" y="158" font-size="7.5" font-weight="700">555 010 0000</text>
      <text x="81" y="177" font-size="7.5" font-weight="700">Your location</text>
    </g>
    <rect x="0" y="186" width="351" height="14" fill="var(--red)"/>
    <polygon points="170,200 188,184 194,184 176,200" fill="var(--red-deep)"/>
    <polygon points="180,200 198,184 202,184 184,200" fill="var(--navy-deep)"/>
    <text x="343" y="196" text-anchor="end" class="serif" font-size="7.5" fill="var(--white)">TRAVEL CARD</text>
  </svg>
</div>

<!-- Health card -->
<div class="piece health-card">
  <svg viewBox="0 0 353 202">
    <rect width="353" height="202" fill="var(--navy)"/>
    <rect x="0" width="24" height="202" fill="var(--red-bright)"/>
    <text transform="translate(16,132) rotate(-90)" class="serif" font-size="9.5" fill="var(--white)">Health Card</text>
    <path d="M353 61 H172 a40 40 0 0 0 0 80 H353" fill="none" stroke="var(--red-bright)" stroke-width="9"/>
    <circle cx="187" cy="101" r="9" fill="var(--navy-deep)"/>
    <text x="202" y="108" class="sans" font-size="19" font-weight="700" fill="var(--grey)">LRC</text>
    <text x="298" y="98" text-anchor="middle" class="sans" font-size="9.5" font-weight="700" fill="var(--red)">LARKMOOR RELIEF</text>
    <line x1="258" y1="108" x2="267" y2="108" stroke="var(--grey)"/>
    <line x1="329" y1="108" x2="338" y2="108" stroke="var(--grey)"/>
    <text x="298" y="111" text-anchor="middle" class="sans" font-size="8" fill="var(--grey)">COOPERATIVE</text>
  </svg>
</div>

<!-- Business card split -->
<div class="piece card-split">
  <svg viewBox="0 0 353 201">
    <rect width="353" height="201" fill="var(--navy)"/>
    <polygon points="0,0 179,0 179,86 197,101 179,116 179,201 0,201" fill="var(--red-bright)"/>
    <g class="serif" fill="var(--white)" text-anchor="end">
      <text x="116" y="58" font-size="12" font-weight="700">Maren Tolliver</text>
      <text x="116" y="68" font-size="9.5">Creative Design</text>
      <text x="116" y="92" font-size="9.5" font-weight="700">555 010 0000</text>
      <text x="116" y="119" font-size="9.5" font-weight="700">Your location</text>
      <text x="116" y="146" font-size="9.5" font-weight="700">tolliver@lrc.com</text>
    </g>
    <g fill="var(--navy)" stroke="var(--white)" stroke-width="1.5">
      <rect x="126" y="49" width="21" height="21" rx="3"/>
      <rect x="126" y="77" width="21" height="21" rx="3"/>
      <rect x="126" y="105" width="21" height="21" rx="3"/>
      <rect x="126" y="132" width="21" height="21" rx="3"/>
    </g>
    <g fill="var(--white)">
      <circle cx="136.5" cy="56" r="2.8"/>
      <path d="M131 65 a5.5 4.5 0 0 1 11 0z"/>
      <path d="M131 83 l2.5 -1 1.8 2.5 -1.2 1.2 a6 6 0 0 0 3.5 3.5 l1.2 -1.2 2.5 1.8 -1 2.5 c-5.5 0 -9.3 -3.8 -9.3 -9.3z"/>
      <path d="M136.5 109 a3.5 3.5 0 0 1 3.5 3.5 c0 2.5 -3.5 7 -3.5 7 s-3.5 -4.5 -3.5 -7 a3.5 3.5 0 0 1 3.5 -3.5z"/>
      <rect x="131" y="137" width="11" height="11" rx="1"/>
    </g>
    <circle cx="242" cy="86" r="9" fill="var(--navy-deep)"/>
    <text x="257" y="93" class="sans" font-size="20" font-weight="700" fill="var(--grey)">LRC</text>
    <text x="271" y="119" text-anchor="middle" class="sans" font-size="11" font-weight="700" fill="var(--red)">LARKMOOR RELIEF</text>
    <line x1="222" y1="128" x2="233" y2="128" stroke="var(--grey)"/>
    <line x1="309" y1="128" x2="320" y2="128" stroke="var(--grey)"/>
    <text x="271" y="131" text-anchor="middle" class="sans" font-size="9" fill="var(--grey)">COOPERATIVE</text>
  </svg>
</div>

<!-- Booklet cover -->
<div class="piece booklet-cover">
  <svg viewBox="0 0 251 355">
    <defs>
      <linearGradient id="coverDark" x1="0" y1="0" x2="1" y2="1">
        <stop offset="0" stop-color="#5a5a5a"/>
        <stop offset="1" stop-color="#1e1e1e"/>
      </linearGradient>
    </defs>
    <rect width="251" height="355" fill="url(#coverDark)"/>
    <polygon points="0,0 143,0 43,140 0,110" fill="#f4f4f4"/>
    <polygon points="0,110 43,140 173,238 120,355 0,355" fill="#3a3a3a" opacity="0.6"/>
    <polygon points="173,238 251,100 251,200 210,355 150,355" fill="#262626"/>
    <polygon points="190,260 251,180 251,230 215,300" fill="#4a4a4a" opacity="0.6"/>
    <polygon points="143,0 251,0 251,100 173,238 43,140" fill="var(--red)"/>
    <circle cx="20" cy="22" r="11" fill="var(--navy)"/>
    <text x="20" y="25" text-anchor="middle" class="sans" font-size="6" font-weight="700" fill="var(--white)">LRC</text>
    <text x="37" y="21" class="sans" font-size="6" font-weight="700" fill="var(--red)">LARKMOOR RELIEF</text>
    <text x="41" y="27" class="sans" font-size="4.5" fill="var(--grey)">COOPERATIVE</text>
    <text x="6" y="70" class="serif" font-size="8.5" fill="var(--grey)">YOUR IMAGES</text>
    <text x="228" y="90" text-anchor="end" class="serif" font-size="25" fill="var(--white)">Your title</text>
    <text x="18" y="226" class="serif" font-size="16" font-weight="700" fill="var(--white)">yout text</text>
    <g class="serif" font-size="8" fill="var(--white)" letter-spacing="0.6">
      <text x="16" y="243">in content with a descrptoin</text>
      <text x="16" y="255">of  the  compenybrieffly.</text>
      <text x="16" y="267">as well as contact person</text>
    </g>
  </svg>
</div>

<!-- Letterhead -->
<div class="piece letterhead">
  <svg viewBox="0 0 247 351">
    <rect width="247" height="351" fill="var(--white)"/>
    <rect x="0" width="14" height="351" fill="var(--red-bright)"/>
    <polygon points="0,0 4,0 4,40 0,46" fill="var(--red-deep)"/>
    <polygon points="0,60 10,48 14,56 14,70 4,80 0,80" fill="#f04a44"/>
    <polygon points="0,300 4,296 4,351 0,351" fill="var(--red-deep)"/>
    <circle cx="37" cy="25" r="10" fill="var(--navy)"/>
    <text x="37" y="28" text-anchor="middle" class="sans" font-size="6" font-weight="700" fill="var(--white)">LRC</text>
    <text x="44" y="41" text-anchor="middle" class="sans" font-size="5.5" font-weight="700" fill="var(--red)">LARKMOOR RELIEF</text>
    <text x="44" y="48" text-anchor="middle" class="sans" font-size="4.5" fill="var(--grey)">COOPERATIVE</text>
  </svg>
</div>

</body>
</html>
```